Business Card for New Convenience Store

We need a business card for our new convenience store using our logo. We want to have a color scheme and back ground created that will be transferable to other media platforms and advertising.

Industry/Entity Type

Convenience Store

```html
<!DOCTYPE html>
<html lang="en">
<head>
<meta charset="utf-8">
<title>KMS Aldervale – Business Card</title>
<link href="https://fonts.googleapis.com/css2?family=Open+Sans:wght@400;600;800&display=swap" rel="stylesheet">
<style>
  :root {
    --page-bg: #e9e6e2;
    --brown-dark: #4f3422;
    --brown-mid: #8a6446;
    --brown-light: #9a7354;
    --ink: #1c1c1c;
    --paper: #ffffff;
    --sky: #aab6d6;
    --building: #8c6a4c;
  }
  html, body {
    margin: 0;
    width: 1200px;
    height: 1000px;
    overflow: hidden;
    background: var(--page-bg);
    font-family: "Open Sans", Arial, sans-serif;
  }
  .canvas { position: relative; width: 1200px; height: 1000px; }

  .card { position: absolute; overflow: hidden; }
  .card svg.card-art { position: absolute; inset: 0; }

  /* Front */
  .card-front { left: 35px; top: 15px; width: 830px; height: 488px; }
  .brand {
    position: absolute;
    display: flex;
    align-items: center;
    gap: 14px;
    font-weight: 800;
    line-height: 1;
  }
  .brand-mark { border-radius: 50%; flex: none; }
  .brand-name { display: flex; flex-direction: column; }
  .brand-name .main { letter-spacing: 2px; }
  .brand-name .sub { letter-spacing: 1px; margin-top: 4px; }

  .card-front .brand { left: 285px; top: 370px; color: var(--paper); }
  .card-front .brand-mark { width: 36px; height: 36px; background: var(--paper); }
  .card-front .brand-name .main { font-size: 66px; }
  .card-front .brand-name .sub { font-size: 22px; }

  /* Back */
  .card-back { left: 332px; top: 505px; width: 831px; height: 485px; background: var(--paper); }
  .contact { position: absolute; left: 25px; color: var(--paper); }
  .contact-name { top: 30px; font-size: 28px; font-weight: 600; color: var(--ink); margin: 0; }
  .contact-title { top: 70px; font-size: 20px; margin: 0; }
  .contact-address { top: 317px; font-size: 20px; line-height: 30px; margin: 0; font-style: normal; }
  .contact-lines { top: 395px; margin: 0; padding: 0; list-style: none; font-size: 20px; line-height: 34px; }
  .contact-lines li { display: flex; align-items: center; gap: 10px; }
  .contact-lines svg { width: 16px; height: 16px; }

  .card-back .brand { left: 430px; top: 180px; color: var(--ink); gap: 16px; }
  .card-back .brand-mark { width: 40px; height: 40px; background: var(--ink); }
  .card-back .brand-name .main { font-size: 100px; }
  .card-back .brand-name .sub { font-size: 30px; }
</style>
</head>
<body>
<main class="canvas">

  <section class="card card-front" aria-label="Card front">
    <svg class="card-art" width="830" height="488" viewBox="0 0 830 488" aria-hidden="false">
      <defs>
        <linearGradient id="photoTone" x1="0" y1="0" x2="0" y2="1">
          <stop offset="0" stop-color="var(--sky)"/>
          <stop offset="0.35" stop-color="#b9b7b8"/>
          <stop offset="0.5" stop-color="var(--building)"/>
          <stop offset="1" stop-color="#6f5540"/>
        </linearGradient>
        <linearGradient id="bandFront" x1="0" y1="0" x2="1" y2="0">
          <stop offset="0" stop-color="var(--brown-dark)"/>
          <stop offset="0.55" stop-color="var(--brown-light)"/>
          <stop offset="1" stop-color="var(--brown-dark)"/>
        </linearGradient>
      </defs>
      <rect class="store-photo" width="830" height="360" fill="url(#photoTone)" role="img" aria-label="Photo of the new convenience store exterior with customers at the entrance"/>
      <path class="wave-stripe-dark" d="M0 283 C150 313 280 383 420 363 C560 343 680 253 830 258 V276 C680 272 560 360 420 380 C280 400 150 330 0 300 Z" fill="var(--ink)"/>
      <path class="wave-stripe-light" d="M0 296 C150 326 280 396 420 376 C560 356 680 266 830 271 V282 C680 278 560 366 420 386 C280 406 150 336 0 306 Z" fill="var(--paper)"/>
      <path class="wave-band" d="M0 304 C150 334 280 404 420 384 C560 364 680 274 830 279 V488 H0 Z" fill="url(#bandFront)"/>
    </svg>
    <div class="brand">
      <span class="brand-mark"></span>
      <span class="brand-name"><span class="main">KMS</span><span class="sub">ALDERVALE</span></span>
    </div>
  </section>

  <section class="card card-back" aria-label="Card back">
    <svg class="card-art" width="831" height="485" viewBox="0 0 831 485">
      <defs>
        <linearGradient id="bandBack" x1="0" y1="0" x2="0" y2="1">
          <stop offset="0" stop-color="var(--brown-dark)"/>
          <stop offset="0.45" stop-color="var(--brown-mid)"/>
          <stop offset="1" stop-color="var(--brown-dark)"/>
        </linearGradient>
      </defs>
      <path class="curve-line-outer" d="M420 0 C465 60 455 160 395 240 C335 320 345 420 435 485" fill="none" stroke="var(--ink)" stroke-width="4"/>
      <path class="curve-line-mid" d="M405 0 C450 60 440 160 380 240 C320 320 330 420 420 485" fill="none" stroke="var(--brown-mid)" stroke-width="4"/>
      <path class="curve-line-inner" d="M395 0 C440 60 430 160 370 240 C310 320 320 420 410 485" fill="none" stroke="var(--ink)" stroke-width="3"/>
      <path class="contact-panel" d="M0 0 H383 C428 60 418 160 358 240 C298 320 308 420 398 485 H0 Z" fill="url(#bandBack)"/>
    </svg>

    <h1 class="contact contact-name">Dana Whitfield</h1>
    <p class="contact contact-title">Manager</p>
    <address class="contact contact-address">47 Willow Bend Rd.<br>Aldervale, AL 36555</address>
    <ul class="contact contact-lines">
      <li>
        <svg viewBox="0 0 16 16" aria-hidden="true"><path d="M2 5 C2 3 4 2 8 2 C12 2 14 3 14 5 L11 6 L10 4.5 H6 L5 6 Z M4 8 H12 L13 14 H3 Z" fill="#fff"/></svg>
        <span>555-014-2700</span>
      </li>
      <li>
        <svg viewBox="0 0 16 16" aria-hidden="true"><rect x="1.5" y="3.5" width="13" height="9" fill="none" stroke="#fff"/><path d="M1.5 3.5 L8 9 L14.5 3.5" fill="none" stroke="#fff"/></svg>
        <span>dwhitfield@kmsmarket.com</span>
      </li>
    </ul>

    <div class="brand">
      <span class="brand-mark"></span>
      <span class="brand-name"><span class="main">KMS</span><span class="sub">ALDERVALE</span></span>
    </div>
  </section>

</main>
</body>
</html>
```